CBD oil label, sleek, clean, serious

I need graphic design for a CBD oil company. Black and white labels for 30ml amber color dropper bottles. looking for something that stands out in its simplicity. this product will be a top of the line, highest margin due to quality of ingredients. It should look rich. other products on the shelf use a lot of color and logos. this label should be clear and stand out as a place to rest your eyes in a sea of marketing glitz.

please see the idea board.

Target Market(s)

middle to older adults

Industry/Entity Type

Health And Wellness

Font styles to use
Serif

Colors
fff5ef
cadf82

Requirements
Must have
• We want the look of elegance and like an apothecary label
• Product name will be VellaSharp or VellaSoothe
• see other details on the attached idea board
Nice to have
• think Morvay and old style apothecary with a modern aesthetic
Should not have
• any reference or drawing of cannabis

```html
<!DOCTYPE html>
<html lang="en">
<head>
<meta charset="utf-8">
<title>VellaSoothe Full Spectrum CBD Oil Label</title>
<link href="https://fonts.googleapis.com/css2?family=Source+Sans+3:wght@300;400;600;700&display=swap" rel="stylesheet">
<style>
  :root {
    --backdrop: #d9d9d9;
    --label: #ffffff;
    --ink: #1c1c1c;
    --ink-soft: #2e2e2e;
    --rule: #9a9a9c;
  }
  * { margin: 0; padding: 0; box-sizing: border-box; }
  html, body {
    width: 1200px; height: 800px; overflow: hidden;
    background: var(--backdrop);
    font-family: "Source Sans 3", sans-serif;
    color: var(--ink);
  }
  .label {
    position: absolute; left: 31px; top: 65px;
    width: 987px; height: 471px;
    background: var(--label);
  }
  .label > * { position: absolute; }

  /* Left panel */
  .contents-title {
    left: 31px; top: 71px;
    font-size: 15px; font-weight: 700; letter-spacing: 1.6px;
  }
  .contents-group {
    left: 33px;
    font-size: 15px; font-weight: 300; letter-spacing: 1.5px; line-height: 18.5px;
    color: var(--ink-soft);
  }
  .group-1 { top: 96px; }
  .group-2 { top: 156px; }
  .group-3 { top: 210px; }
  .storage {
    left: 37px; top: 362px;
    font-size: 15px; font-weight: 700; letter-spacing: 1.6px;
  }
  .badges { left: 34px; top: 400px; display: flex; }
  .badge { width: 60px; display: flex; flex-direction: column; align-items: flex-start; }
  .badge:nth-child(4) { margin-left: -6px; }
  .badge svg { width: 28px; height: 28px; margin-left: 0; }
  .badge span {
    font-size: 7px; letter-spacing: 0.8px; line-height: 7.5px; margin-top: 2px;
    color: var(--ink-soft); text-align: center; min-width: 28px;
  }

  /* Brand block */
  .brand-box {
    left: 333px; top: 64px; width: 304px; height: 71px;
    border: 2px solid var(--rule);
    display: flex; align-items: center; justify-content: center;
  }
  .brand-name {
    font-size: 30px; font-weight: 700; letter-spacing: 7.5px; padding-left: 7px;
  }
  .tier {
    left: 334px; top: 151px;
    display: flex; align-items: center; width: 304px;
  }
  .tier-word { font-size: 13px; font-weight: 400; letter-spacing: 10px; }
  .tier-bar { flex: 1; height: 10px; background: var(--rule); margin-left: -6px; }

  /* Product block */
  .product { left: 333px; top: 220px; width: 304px; text-align: center; }
  .product-name { font-size: 31px; letter-spacing: 6px; line-height: 40px; white-space: nowrap; }
  .product-name .light { font-weight: 300; }
  .product-name .bold { font-weight: 700; }
  .product-kind { font-size: 14px; letter-spacing: 2px; margin-top: 8px; }
  .product-type { font-size: 22px; font-weight: 700; letter-spacing: 1.5px; margin-top: 1px; }
  .volume { font-size: 19px; font-weight: 600; margin-top: 47px; }
  .flavor { font-size: 14px; letter-spacing: 4px; margin-top: 5px; }

  /* Directions */
  .directions {
    top: 30px; height: 398px;
    writing-mode: vertical-rl; transform: rotate(180deg);
    font-size: 13.2px; font-weight: 300; line-height: 18.6px;
    color: var(--ink);
  }
  .directions strong { font-weight: 700; }
  .directions-use { left: 787px; width: 76px; }
  .directions-caution { left: 879px; width: 40px; }
  .bullet {
    top: 432px; width: 10px; height: 10px; border-radius: 50%;
    background: var(--ink);
  }
  .bullet-use { left: 789px; }
  .bullet-caution { left: 882px; }
</style>
</head>
<body>
<main class="label">
  <p class="contents-title">Food Supplement Contains:</p>
  <p class="contents-group group-1">Full Spectrum CBD,<br>Hemp oil and Natural flavor</p>
  <p class="contents-group group-2">CBD derived from Cannabis<br>less than 0.025 THC</p>
  <p class="contents-group group-3">Derived from Cannabis<br>as a full spectrum oil</p>

  <p class="storage">Store in a cool, dark place</p>

  <div class="badges">
    <div class="badge">
      <svg viewBox="0 0 28 28" aria-hidden="true">
        <circle cx="14" cy="14" r="12.5" fill="none" stroke="#1c1c1c" stroke-width="1.6"/>
        <path d="M8 18c5 0 10-3 12-9-6 0-11 3-12 9z" fill="#1c1c1c"/>
        <path d="M12 10c-2-2-4-2-5-1 0 2 2 4 5 4z" fill="#1c1c1c"/>
      </svg>
      <span>Vegan</span>
    </div>
    <div class="badge">
      <svg viewBox="0 0 28 28" aria-hidden="true">
        <circle cx="14" cy="14" r="12.5" fill="none" stroke="#1c1c1c" stroke-width="1.6"/>
        <line x1="5" y1="5" x2="23" y2="23" stroke="#1c1c1c" stroke-width="1.6"/>
      </svg>
      <span>Non<br>GMO</span>
    </div>
    <div class="badge">
      <svg viewBox="0 0 28 28" aria-hidden="true">
        <circle cx="14" cy="14" r="12.5" fill="none" stroke="#1c1c1c" stroke-width="1.6"/>
        <path d="M14 5c-4 5-6 8-6 11a6 6 0 0 0 12 0c0-3-2-6-6-11z" fill="none" stroke="#1c1c1c" stroke-width="1.4"/>
        <line x1="14" y1="9" x2="14" y2="21" stroke="#1c1c1c" stroke-width="1.2"/>
      </svg>
      <span>Pure<br>CBD</span>
    </div>
    <div class="badge">
      <svg viewBox="0 0 28 28" aria-hidden="true">
        <circle cx="14" cy="14" r="12.5" fill="#1c1c1c"/>
        <path d="M7 20c3-8 8-11 14-12-1 7-6 11-12 11z" fill="#fff"/>
        <line x1="7" y1="21" x2="17" y2="12" stroke="#1c1c1c" stroke-width="1.2"/>
      </svg>
      <span>Natural<br>Ingredients</span>
    </div>
  </div>

  <div class="brand-box"><span class="brand-name">ALDER VALE</span></div>
  <div class="tier"><span class="tier-word">PREMIUM</span><span class="tier-bar"></span></div>

  <section class="product">
    <h1 class="product-name"><span class="light">Vella</span><span class="bold">SOOTHE</span></h1>
    <p class="product-kind">FULL SPECTRUM</p>
    <p class="product-type">CBD OIL</p>
    <p class="volume">30 ml &nbsp;|&nbsp; 1000 mg</p>
    <p class="flavor">MINT FLAVOR</p>
  </section>

  <p class="directions directions-use"><strong>Use:</strong> Shake well. Take 1 dropper to the mark twice daily. Hold under the tongue for 30 seconds. Use every day for best results. Start CBD use with a half dose and work up to full dose after 7 days.</p>
  <span class="bullet bullet-use"></span>
  <p class="directions directions-caution">Discuss CBD use with a physician if taking other medications. Do not exceed 5 doses in a day</p>
  <span class="bullet bullet-caution"></span>
</main>
</body>
</html>
```